Real Estate "For Sale" Sign for construction company

We need a sign that we can use to hang on a post and place on the road when we sell a property. The sign will be simple and will need to mainly feature our logo (files attached), as well as the words "For Sale", and then our phone number "(555) 617 3489". The sign will hang on a post that'll look something like the attached picture.

Target Market(s)

Home buyers

Industry/Entity Type

Real Estate

Font styles to use
Serif
Sans Serif

Colors
0054AA
0677BA
7BADD7
CADEEF
E8F1F8
0094D4
00A9DD
6FCCEA
C7EBF8
E9F6FB

Requirements
Must have
• For Sale & our phone number

```html
<!DOCTYPE html>
<html lang="en">
<head>
<meta charset="utf-8">
<title>For Sale Sign</title>
<link rel="stylesheet" href="https://fonts.googleapis.com/css2?family=Montserrat:wght@800&display=swap">
<style>
  :root {
    --navy: #2f3454;
    --cyan: #4fc8f4;
    --white: #ffffff;
    --brand-mid: #0677ba;
    --backdrop-top: #f3f4f6;
    --backdrop-bottom: #b6e4f6;
  }
  html, body {
    margin: 0;
    padding: 0;
    width: 1200px;
    height: 957px;
    overflow: hidden;
  }
  body {
    background: linear-gradient(180deg, var(--backdrop-top) 0%, #eef3f6 55%, var(--backdrop-bottom) 100%);
  }
  .sign {
    display: block;
    width: 1200px;
    height: 957px;
  }
  .headline,
  .phone {
    font-family: "Montserrat", sans-serif;
    font-weight: 800;
    fill: var(--white);
  }
  .brand-name {
    font-family: "Montserrat", sans-serif;
    font-weight: 800;
    fill: var(--navy);
  }
</style>
</head>
<body>
<svg class="sign" viewBox="0 0 1200 957" xmlns="http://www.w3.org/2000/svg" role="img" aria-label="For Sale sign with phone number (555) 617 3489">
  <rect class="board" x="80" y="88" width="1040" height="781" fill="var(--white)"/>
  <rect class="top-band" x="80" y="88" width="1040" height="40" fill="var(--cyan)"/>

  <polygon class="headline-banner" points="80,167.5 886,167.5 999,375 885,578 80,578" fill="var(--navy)"/>
  <polygon class="headline-chevron" points="910,167.5 931,167.5 1044,375 929,578 908,578 1023,375" fill="var(--navy)"/>
  <text class="headline" x="122" y="434.5" font-size="166" textLength="768" lengthAdjust="spacingAndGlyphs">FOR SALE</text>

  <polygon class="phone-banner" points="447,737 561,637.5 1120,637.5 1120,832.7 562,832.7" fill="var(--navy)"/>
  <text class="phone" x="520" y="760" font-size="82" textLength="564" lengthAdjust="spacingAndGlyphs">(555) 617 3489</text>

  <rect class="brand-mark" x="112" y="722" width="20" height="20" fill="var(--brand-mid)"/>
  <text class="brand-name" x="142" y="742" font-size="26">Ridgeline Crest</text>
</svg>
</body>
</html>
```